Relaunch / Responsives, modernes Webdesign für ein Campingportal
Zielgruppe
Die zeltfuchs GmbH betreibt mit der Plattform www.zeltfuchs.de eines der führenden Campingportale in Deutschland.
Im Zuge des Relaunches soll ein frisches, neues und modernes Design der Webseite erfolgen und auch die mobile Nutzbarkeit durch ein responsives Design verbessert werden.
Zielgruppe sind Camperinnen und Camper bzw. solche, die es vielleicht einmal werden wollen. Ebenso natürlich auch die Betreiber der Campingplätze, die Mitglied bei zeltfuchs sein können und damit bei der Suche, auf der Karte und in den Regionen gefunden werden. Sie sind dann mit einer eigenen Campingplatzseite vertreten, auf der neben allen wichtigen Informationen auch Bilder und Videos vom Platz zu sehen sind.
Aktuell ist im Fokus ein Campingführer (Campingplatzsuche), der wie beschrieben auch per Karte erfolgt und mit Filtern eingeschränkt werden kann. Auch ein Blog ist vorhanden, es wird noch ein Forum geben usw.
Später wird auch noch ein Shop, etc. hinzukommen...
Aufgabenstellung
Das Design soll frisch, modern und natürlich responsiv sein. Das Logo ist dabei weiterhin gesetzt. Daran können Sie also z.B. die Farbgebung übernehmen (v.a. das Grün).
Das Design soll sich nicht mehr rein vertikal ausrichten (wie bisher) sondern horizontal über den gesamten Bildschirm.
Dabei muss z.B. auf der Startseite u.a. auch ein Feld vorhanden sein, in dem man Länder, Regionen oder direkt Campingplätze suchen kann uns sich ein Auswahlfeld mit den vorgeschlagenen Ergebnissen öffnet. So wie bei Hotelportalen zumeist auch.
Es gibt aktuell nachfolgende Seitentypen:
1. Startseite (bisher http://www.zeltfuchs.de/)
Hier soll u.a. auch ein Feld zur Eingabe eines Landes, einer Region oder eines Platzes existieren, bei dem bei Eingabe Auswahlmöglichkeiten sichtbar werden (wie bei Reiseportalen).
So z.B. bei:
Urlaubsquartier[Punkt]de
Stubo Nahweg
Tripbewerter
Auch eine Karte von Europa wäre hier ggf. interessant, die man dann beim Anklicken auf Deutschland fokussiert, danach dann weiter auf die Nordsee usw.
Zudem Flächen wo man besondere Themen oder Regionen noch einmal extra anführt "Campingplätze am Meer", "Campingplätze in den Bergen", "Campingplätze Stadtnah, usw.
Hier zum Beispiel dann auch später eine Grafik zum Shop usw.
Auch kann es einige Flächen geben, die man an Campingplätze vermieten kann, um auf der Startseite präsent zu sein. Also quasi einige exklusive Campingplätze.
Zudem sollte man einen Block haben, wo man besonders nachgefragte Regionenlinks vorstellen kann (Beliebte Reiseziele, Nordseeküste, Alpen, etc.).
Dies müssen aber keine Bilder sein, sondern können auch nur Links sein als Gruppe in einem Block.
Zudem muss es unten ein Textfeld geben, da es sonst schwer wird mit der Regionenseite bei Suchraum weiterhin gut zu ranken.
Selbstverständlich müssen auch Werbeflächen eingeplant sein für Suchraum adse..

```html
<!DOCTYPE html>
<html lang="de">
<head>
<meta charset="utf-8">
<title>zeltfuchs – Camping Elbufer Strand</title>
<link href="https://fonts.googleapis.com/css2?family=Open+Sans:wght@400;600;700&family=Titillium+Web:wght@600;700&display=swap" rel="stylesheet">
<style>
:root{
  --green:#93c01f;
  --green-dark:#83ad17;
  --navy:#1d2557;
  --text:#555b61;
  --muted:#8a8f94;
  --light:#f1f1f1;
  --line:#e4e4e4;
  --white:#fff;
  --footer:#4d4d4f;
  --link-blue:#1a6fd1;
}
*{box-sizing:border-box;margin:0;padding:0}
html,body{width:1200px;height:3788px;overflow:hidden}
body{position:relative;font-family:"Open Sans",sans-serif;font-size:11px;color:var(--text);background:var(--white)}
.abs{position:absolute}
h2,h3,.display{font-family:"Titillium Web",sans-serif;font-weight:700}
a{color:inherit;text-decoration:none}
ul{list-style:none}

/* header */
.site-header{top:0;left:0;width:1200px;height:82px;background:var(--white)}
.brand{left:41px;top:27px;display:flex;align-items:center;gap:8px}
.brand-mark{width:22px;height:22px;background:var(--navy);border-radius:50%}
.brand-name{font-family:"Titillium Web",sans-serif;font-weight:700;font-size:24px;color:var(--green);line-height:1}
.main-nav{left:426px;top:36px;display:flex;gap:48px;font-size:11px;font-weight:600;color:var(--navy)}
.main-nav .active{color:var(--navy);border-bottom:2px solid var(--green);padding-bottom:4px}
.btn-login{left:1050px;top:25px;width:107px;height:34px;background:var(--green);color:#fff;font-weight:700;font-size:11px;display:flex;align-items:center;justify-content:center}

/* search */
.search-band{top:82px;left:0;width:1200px;height:71px;background:var(--green)}
.search-label{left:41px;top:24px;color:#fff}
.search-label strong{display:block;font-family:"Titillium Web",sans-serif;font-size:17px;line-height:1}
.search-label span{font-size:9px}
.search-input{left:166px;top:24px;width:716px;height:36px;background:#fff;font-size:9px;color:var(--muted);padding:12px 16px}
.search-select{left:901px;top:24px;width:121px;height:36px;background:#fff;font-size:9px;color:var(--muted);padding:12px 14px}
.search-select i{position:absolute;right:8px;top:11px;width:16px;height:14px;background:var(--light)}
.btn-search{left:1046px;top:24px;width:111px;height:36px;background:var(--navy);color:#fff;font-size:9px;font-weight:700;display:flex;align-items:center;justify-content:center}

/* hero */
.hero{top:153px;left:0;width:1200px;height:341px;background:linear-gradient(180deg,#e9c9a7 0%,#c7cfd8 35%,#7fa1b7 55%,#3d6e88 72%,#2b3b45 100%)}
.hero-arrow{top:147px}
.hero-title{left:124px;top:255px;font-size:35px;color:#fff;line-height:1}
.hero-stars{left:534px;top:269px;display:flex;gap:2px}
.hero-badge{left:663px;top:233px;width:58px;height:58px;border-radius:50%;background:#fff;border:4px solid var(--green)}
.breadcrumb{display:flex;align-items:center;gap:6px;font-size:9px}
.hero .breadcrumb{left:128px;top:307px;color:#fff}

/* tabs */
.tab-bar{top:494px;left:0;width:1200px;height:59px;background:var(--green)}
.tabs{left:125px;top:18px;display:flex;gap:25px;font-size:11px;font-weight:700;color:#fff}
.tabs li{padding:5px 0}
.tabs .active{background:var(--navy);padding:5px 9px}
.btn-video{left:832px;top:0;width:242px;height:59px;background:var(--navy);color:#fff;font-size:11px;font-weight:700;display:flex;align-items:center;justify-content:center;gap:7px}

/* main column */
.section-title{font-size:20px;color:var(--green);line-height:1}
.desc{left:124px;top:585px;width:684px}
.desc h3{font-family:"Open Sans",sans-serif;font-size:11px;font-weight:700;color:#4b5055;margin:22px 0 8px}
.desc p{font-size:10.5px;line-height:19px}
.photos-title{left:124px;top:1355px}
.photo{width:206px;height:137px}
.photo-beach{background:linear-gradient(180deg,#c0524a 0%,#d99a8e 25%,#c7d5e0 45%,#eceae3 70%,#c2b59b 100%)}
.photo-van{background:linear-gradient(135deg,#1c2c36 0%,#5c6d6a 45%,#d6c68f 55%,#2c3f3a 100%)}
.photo-sea{background:linear-gradient(180deg,#b6c7d1 0%,#6b8ba0 40%,#34566e 75%,#223c4f 100%)}
.infos-title{left:124px;top:1748px}
.info-table{left:124px;top:1800px;width:684px}
.info-table h4,.ground h4{font-size:11px;font-weight:700;color:#3e4347;margin-bottom:10px}
.info-table li{display:flex;font-size:10.5px;height:25px;line-height:25px}
.info-table li span:first-child{width:480px}
.info-rule{left:124px;top:2025px;width:647px;height:2px;background:var(--green)}
.ground{left:124px;top:2064px}
.ground li{display:flex;font-size:10.5px;height:25px;line-height:25px}
.ground b{width:90px;color:#3e4347}
.ground span{width:90px}

/* sidebar */
.sidebar{top:553px;left:832px;width:242px;height:1632px;background:var(--light)}
.side-block{left:30px;width:200px}
.side-block h3{font-size:15px;color:var(--green);margin-bottom:14px;line-height:1}
.side-block p{font-size:10.5px;line-height:16px}
.side-block p b{color:var(--navy);font-weight:700}
.side-block .entry{margin-bottom:14px}
.side-links li{font-size:10.5px;font-weight:700;color:var(--navy);margin-bottom:7px;display:flex;gap:5px;align-items:center}
.side-links i{width:9px;height:9px;background:var(--green);display:inline-block}
.ticks li{font-size:10.5px;display:flex;gap:6px;align-items:center;height:25px}
.badges{left:30px;top:960px;display:grid;grid-template-columns:80px 80px;gap:20px 20px}
.badge-round{width:58px;height:58px;border-radius:50%;background:#fff;border:4px solid var(--green);margin-left:10px}
.badge-card{width:72px;height:48px;background:#f3c21b;margin-top:5px}
.badge-blob{width:62px;height:52px;border-radius:50%;background:#2a8ed0}
.badge-square{width:76px;height:58px;background:#5aa62d}
.ad-side{left:16px;top:1184px;width:212px;height:424px;background:#fff;padding:4px}
.ad-side .ad-head{height:115px;border-bottom:1px solid var(--line);position:relative;padding:22px 4px 0}
.ad-big{font-size:18px;color:var(--link-blue);line-height:21px;width:140px}
.ad-small{font-size:9px;color:#333;margin-top:6px;line-height:11px}
.ad-go{position:absolute;right:10px;top:27px;width:34px;height:34px;background:#333}
.ad-list li{height:44px;border-bottom:1px solid var(--line);font-size:18px;color:var(--link-blue);line-height:21px;padding:5px 4px;display:flex;justify-content:space-between;align-items:center}
.ad-list li::after{content:"›";color:#aaa;font-size:12px;padding-right:20px}

/* nearby */
.nearby{top:2259px;left:0;width:1200px;height:650px;background:var(--light)}
.nearby-title{top:73px;width:1200px;text-align:center;font-size:21px;color:var(--green)}
.nearby-sub{top:102px;width:1200px;text-align:center;font-size:10.5px;line-height:19px}
.slider-btn{top:366px;width:41px;height:41px;background:var(--navy);display:flex;align-items:center;justify-content:center}
.card{top:175px;width:302px;height:416px;background:#fff}
.card-img{height:157px;position:relative}
.card-img .seal{position:absolute;left:22px;top:20px;width:56px;height:56px;border-radius:50%;background:#fff;border:4px solid var(--green)}
.img-mountain{background:linear-gradient(180deg,#e8eaea 0%,#9aa4a6 35%,#4a5a4c 60%,#6c7f57 100%)}
.img-forest{background:linear-gradient(180deg,#d6e6f0 0%,#7fa66a 35%,#3f6d33 70%,#5a7e44 100%)}
.card-body{text-align:center;padding-top:19px}
.card-stars{display:flex;justify-content:center;gap:2px}
.card-name{font-size:15px;color:var(--green);margin-top:10px;line-height:1}
.card-place{font-size:11px;margin-top:8px}
.card .breadcrumb{justify-content:center;margin-top:14px;font-size:9.5px}
.card-text{font-size:10.5px;line-height:19px;margin-top:16px;padding:0 24px}
.card-foot{position:absolute;left:0;bottom:0;width:100%;height:39px;display:flex}
.card-price{flex:1;background:#dcdcdc;color:#fff;font-size:9px;display:flex;align-items:center;justify-content:center;gap:6px}
.card-price b{color:var(--navy)}
.card-more{width:108px;background:var(--green);color:#fff;font-size:9.5px;font-weight:700;display:flex;align-items:center;justify-content:center}

/* directory */
.directory{top:2909px;left:0;width:1200px;height:500px}
.dir-title{left:124px;top:50px;font-size:15px;color:var(--green)}
.dir-group{font-size:9px;line-height:16.5px}
.dir-group h4{font-size:10.5px;font-weight:700;color:#3e4347;margin-bottom:2px}
.dir-group a::before{content:"› ";color:var(--navy);font-weight:700}
.dir-group a{margin-right:6px}
.ad-banner{left:228px;top:363px;width:744px;height:74px;border:1px solid var(--line);padding:10px 7px}
.ad-banner .ad-big{width:auto;font-size:21px}
.ad-banner .ad-go{right:304px;top:10px;width:64px;height:50px;background:#444}
.ad-note{left:228px;top:441px;font-size:7px;color:var(--muted)}

/* shop band */
.shop-band{top:3409px;left:0;width:1200px;height:132px;background:var(--green)}
.shop-text{left:123px;top:53px;font-size:21px;color:#fff;line-height:1}
.btn-shop{left:966px;top:51px;width:107px;height:31px;background:var(--navy);color:#fff;font-size:9.5px;font-weight:700;display:flex;align-items:center;justify-content:center}

/* footer */
.site-footer{top:3541px;left:0;width:1200px;height:206px;background:#fff}
.footer-brand{left:140px;top:80px;display:flex;align-items:center;gap:9px}
.footer-brand .brand-name{font-size:30px}
.footer-col{top:47px}
.footer-col h3{font-size:15px;color:var(--green);line-height:1;margin-bottom:18px}
.footer-col li{font-size:11px;height:25px}
.footer-col li::before{content:"› ";font-weight:700;color:var(--navy)}
.social{left:913px;top:88px;display:flex;gap:23px}
.social i{width:24px;height:24px;border-radius:50%;background:var(--navy);display:block}
.bottom-bar{top:3747px;left:0;width:1200px;height:41px;background:var(--footer);color:#fff;font-size:9.5px}
.bottom-bar span{position:absolute;top:14px}
</style>
</head>
<body>

<header class="abs site-header">
  <div class="abs brand"><span class="brand-mark"></span><span class="brand-name">zeltfuchs</span></div>
  <nav class="abs main-nav"><a class="active">START</a><a>CAMPINGPLÄTZE</a><a>BLOG</a><a>ÜBER UNS</a></nav>
  <a class="abs btn-login">ANMELDEN</a>
</header>

<section class="abs search-band">
  <div class="abs search-label"><strong>SUCHE</strong><span>Campingplatz finden</span></div>
  <div class="abs search-input">Land, Region oder Campingplatz suchen</div>
  <div class="abs search-select">Mitgliedschaft<i></i></div>
  <a class="abs btn-search">JETZT SUCHEN</a>
</section>

<section class="abs hero" role="img" aria-label="Foto: Blick aus einem Zelt auf Strand und Meer bei Sonnenuntergang">
  <svg class="abs hero-arrow" style="left:28px" width="20" height="34" viewBox="0 0 20 34"><path d="M17 2 3 17l14 15" fill="none" stroke="#fff" stroke-width="3"/></svg>
  <svg class="abs hero-arrow" style="left:1152px" width="20" height="34" viewBox="0 0 20 34"><path d="M3 2l14 15L3 32" fill="none" stroke="#fff" stroke-width="3"/></svg>
  <h1 class="abs hero-title display">Camping Elbufer Strand</h1>
  <div class="abs hero-stars">
    <svg width="105" height="19" viewBox="0 0 105 19"><defs><path id="st" d="M9.5 0l2.2 6.6h7l-5.6 4.1 2.1 6.7-5.7-4.1-5.7 4.1 2.1-6.7L.3 6.6h7z"/></defs><g fill="#93c01f"><use href="#st"/><use href="#st" x="21"/><use href="#st" x="42"/><use href="#st" x="63"/><use href="#st" x="84"/></g></svg>
  </div>
  <div class="abs hero-badge"></div>
  <div class="abs breadcrumb"><span>Deutschland</span><span>›</span><span>Niedersachsen</span><span>›</span><span>Lüneburger Heide</span></div>
</section>

<nav class="abs tab-bar">
  <ul class="abs tabs"><li class="active">PROFIL</li><li>LAGE</li><li>AUSSTATTUNG</li><li>FREIZEIT</li><li>MIETUNTERKUNFT</li><li>BEWERTUNG</li><li>KONTAKT</li></ul>
  <a class="abs btn-video"><svg width="13" height="13" viewBox="0 0 13 13"><circle cx="6.5" cy="6.5" r="6.5" fill="#fff"/><path d="M5 4l4 2.5L5 9z" fill="#1d2557"/></svg>JETZT VIDEO ANSCHAUEN</a>
</nav>

<article class="abs desc">
  <h2 class="section-title">Campingplatz-Beschreibung</h2>
  <h3 style="margin-top:18px">Campingplatz Elbufer Strand - in der Nähe von Hamburg</h3>
  <p>Der Campingplatz Elbufer Strand befindet sich in Elbmarsch am Elbstrand der Elbe in der Nähe der Weltstadt Hamburg.<br>Der Platz ist ganzjährig geöffnet. Auf dem Gelände befinden sich ein ebenfalls ganzjährig geöffneter Frischmarkt<br>und eine Gastwirtschaft.</p>
  <p style="margin-top:6px">Die Lage vom Campingplatz Elbufer Strand an der Elbe ermöglicht ein abwechslungsreiches Freizeitprogramm:<br>Sie können in der Parkanlage spazieren gehen, Sie können am Strand sitzen, angeln oder baden. Sie können aber auch<br>ein Fahrrad leihen und in der Marschlandschaft, an der Elbe radeln.</p>
  <h3 style="margin-top:26px">Campingplatz Elbufer Strand - die Ausstattung</h3>
  <p>In dem erneuerten Badehaus vom Campingplatz Elbufer Strand sind sowohl große Waschräume als auch Einzelkabinen. Umkleide- und Toilettenhäuser werden zur Saison aufgestellt. Sie sind komfortabel ausgestattet. Koch- und Abwaschbereich sind im gleichen Gebäude untergebracht wie die Waschküche.<br>Der Campingplatz Elbufer Strand bietet zudem: Bootshafen, Fußball- und Basketballfelder, Grillplätze, Wasserski, Behindertenanlagen, Babywickelraum, Kinderspielplatz mit verschiedenen Spielgeräten, Fahrradverleih, Wohnmobilstellplätze direkt am Wasser incl. Entsorgung, Imbiss, Restaurant und SB-Laden. Außerdem in der Umgebung: Schwimmbad, Tennis, Reiten, Kegelbahn.<br>Als Jahresplätze stehen 450 Plätze zu je 130 qm zur Verfügung. Es stehen zur Verfügung: modernste Sanitäranlagen, Strom- und Wasseranschluss, Kochküche, Münzwaschsalon mit Trockner, Gasverkauf.<br>Die auf dem Campingplatz Elbufer Strand vorhandenen Mietwohnwagen stehen als kostengünstige Unterkunft zur Verfügung. Sie sind mit 4 Schlafplätzen ausgestattet und haben ein großes Vorzelt mit Sitzgruppe. In den Mietwohnwagen darf nicht geraucht werden. Mietmobilheime sind ebenfalls für 4 Personen eingerichtet und haben eine Küchenzeile und ein Badezimmer. Rauchen ist nicht erlaubt, Tierhaltung nur teilweise. Ferienhäuser haben ein Wohnzimmer mit TV, 4 Schlafplätze, eine Küchenzeile und ein Badezimmer. Rauchen und Tierhaltung sind nicht erlaubt.<br>Beim Camping am Elbufer Strand bleiben keine Wünsche offen.</p>
  <h3 style="margin-top:26px">Campingplatz Elbufer Strand - Kulinarisches</h3>
  <p>Auf dem Campingplatz Elbufer Strand befindet sich das gleichnamige Restaurant, das über 120 Sitzplätze verfügt, eine Terrasse und einen Wintergarten mit Kamin. Das Restaurant bietet neben den a la carte- Angeboten fast täglich wechselnde regionale Spezialitäten an.</p>
  <h3 style="margin-top:22px">Campingplatz Elbufer Strand - Animation und Ausflüge</h3>
  <p>Von Mai bis Mitte September wird auf dem Campingplatz Elbufer Strand ein Animationsprogramm angeboten. Dazu kommen viele Feste. Ausflugsziele sind u.a. Hamburg, Lauenburg, Lüneburg, Winsen, Geesthacht. Vom Fahrgastschiffanleger im eigenen Yachthafen werden Fahrten nach Hamburg mit dem größten Hafen Deutschlands und den vielen Sehenswürdigkeiten angeboten.</p>
</article>

<h2 class="abs section-title photos-title">Campingplatz Fotos</h2>
<div class="abs photo photo-beach" style="left:124px;top:1397px" role="img" aria-label="Foto: Strand durch den Zelteingang gesehen"></div>
<div class="abs photo photo-van" style="left:346px;top:1397px" role="img" aria-label="Foto: Abendlicht im Wohnwagenfenster"></div>
<div class="abs photo photo-sea" style="left:566px;top:1397px" role="img" aria-label="Foto: Wellen am Ufer in der Dämmerung"></div>
<div class="abs photo photo-beach" style="left:124px;top:1556px" role="img" aria-label="Foto: Strand durch den Zelteingang gesehen"></div>
<div class="abs photo photo-van" style="left:346px;top:1556px" role="img" aria-label="Foto: Abendlicht im Wohnwagenfenster"></div>
<div class="abs photo photo-sea" style="left:566px;top:1556px" role="img" aria-label="Foto: Wellen am Ufer in der Dämmerung"></div>

<h2 class="abs section-title infos-title">Campingplatz Infos</h2>
<div class="abs info-table">
  <h4>Anzahl der Stellplätze</h4>
  <ul>
    <li><span>Stellplätze [Gesamt]</span><span>500</span></li>
    <li><span>Fest gebucht</span><span>400</span></li>
    <li><span>Frei belegbar</span><span>100</span></li>
    <li><span>Stellplätze ohne Stromanschluss</span><span>k. A.</span></li>
    <li><span>Stellplätze mit Stromanschluss</span><span>100</span></li>
    <li><span>Stellplätze mit Schattendächern</span><span>k. A.</span></li>
    <li><span>Stellplätze mit Frisch-/Abwasseranschluss</span><span>100</span></li>
  </ul>
</div>
<div class="abs info-rule"></div>
<div class="abs ground">
  <h4>Beschaffenheit des Platzes</h4>
  <ul>
    <li><b>Untergrund</b><span>10% Gras</span><span>20% Stein</span><span>10% Sand</span></li>
    <li><b>Schatten</b><span>30% Keiner</span><span>30% Wenig</span><span>30% Normal</span><span>0% Viel</span></li>
    <li><b>Lautstärke</b><span>10% Sehr ruhig</span><span>50% ruhig</span><span>30% etwas lauter</span><span>0% laut</span></li>
  </ul>
</div>

<aside class="abs sidebar">
  <div class="abs side-block" style="top:34px">
    <h3>Kontakt</h3>
    <p><b>Campingplatz Elbufer Strand</b><br>Uferweg 14<br>21499 Elbmarsch<br>Deutschland</p>
    <p style="margin-top:6px"><b>Telefon:</b> +49 (0) 4100 000</p>
    <ul class="side-links" style="margin-top:18px"><li><i></i>Infos anfordern</li><li><i style="border-radius:50%"></i>Zur Homepage</li><li><i></i>Auf Netzwerk teilen</li></ul>
  </div>
  <div class="abs side-block" style="top:287px">
    <h3>Öffnungszeiten</h3>
    <p class="entry"><b>Jährlich geöffnet</b><br>01.01. - 31.12.</p>
    <p class="entry"><b>Check-In Zeiten</b><br>08:00 - 20:00 Uhr</p>
    <p class="entry"><b>Mittagspause</b><br>13:00 - 15:00 Uhr</p>
  </div>
  <div class="abs side-block" style="top:487px">
    <h3>Stellplätze</h3>
    <p class="entry"><b>Stellplätze Gesamt</b><br>500</p>
    <p class="entry"><b>Fest gebuchte Stellplätze</b><br>400</p>
    <p class="entry"><b>Frei belegbare Stellplätze</b><br>100</p>
  </div>
  <div class="abs side-block" style="top:691px">
    <h3>Besonderheiten</h3>
    <ul class="ticks">
      <li><svg width="9" height="8" viewBox="0 0 9 8"><path d="M1 4l2.5 2.5L8 1" fill="none" stroke="#1d2557" stroke-width="2"/></svg>Direkt am Wasser</li>
      <li><svg width="9" height="8" viewBox="0 0 9 8"><path d="M1 4l2.5 2.5L8 1" fill="none" stroke="#1d2557" stroke-width="2"/></svg>Haustier erlaubt</li>
      <li><svg width="9" height="8" viewBox="0 0 9 8"><path d="M1 4l2.5 2.5L8 1" fill="none" stroke="#1d2557" stroke-width="2"/></svg>KCV Campingplatz</li>
      <li><svg width="9" height="8" viewBox="0 0 9 8"><path d="M1 4l2.5 2.5L8 1" fill="none" stroke="#1d2557" stroke-width="2"/></svg>Eco Camping</li>
      <li><svg width="9" height="8" viewBox="0 0 9 8"><path d="M1 4l2.5 2.5L8 1" fill="none" stroke="#1d2557" stroke-width="2"/></svg>Offenes Feuer erlaubt</li>
      <li><svg width="9" height="8" viewBox="0 0 9 8"><path d="M1 4l2.5 2.5L8 1" fill="none" stroke="#1d2557" stroke-width="2"/></svg>zeltfuchs geprüft</li>
      <li><svg width="9" height="8" viewBox="0 0 9 8"><path d="M1 4l2.5 2.5L8 1" fill="none" stroke="#1d2557" stroke-width="2"/></svg>Naturbelassener Campingplatz</li>
      <li><svg width="9" height="8" viewBox="0 0 9 8"><path d="M1 4l2.5 2.5L8 1" fill="none" stroke="#1d2557" stroke-width="2"/></svg>Rabattkarte</li>
    </ul>
  </div>
  <div class="abs badges">
    <div class="badge-round"></div><div class="badge-card"></div>
    <div class="badge-blob"></div><div class="badge-square"></div>
  </div>
  <div class="abs ad-side">
    <div class="ad-head">
      <div class="ad-big">Book A Hotel Tonight</div>
      <div class="ad-small">example.com<br>Special Rates Until the End of the Month. No Booking Fees.</div>
      <span class="ad-go"></span>
    </div>
    <ul class="ad-list"><li>Dublin Hotels</li><li>Hotels in Ireland</li><li>Deals on Hotels</li><li>Free King Bed Upgrade</li><li>Rooms $89 and Up</li><li>Travel Discounts on Hotels</li><li>Cheap Hotel Packages</li></ul>
  </div>
</aside>

<section class="abs nearby">
  <h2 class="abs nearby-title">Top Campingplätze in der Nähe</h2>
  <p class="abs nearby-sub">Diese Campingplätze könnten Sie auch interessieren, sie liegen in der Nähe<br>des momentan gewählten Campingplatz und sind von zeltfuchs geprüft.</p>
  <a class="abs slider-btn" style="left:41px"><svg width="10" height="16" viewBox="0 0 10 16"><path d="M8 1 2 8l6 7" fill="none" stroke="#fff" stroke-width="2"/></svg></a>
  <a class="abs slider-btn" style="left:1117px"><svg width="10" height="16" viewBox="0 0 10 16"><path d="M2 1l6 7-6 7" fill="none" stroke="#fff" stroke-width="2"/></svg></a>

  <div class="abs card" style="left:124px">
    <div class="card-img photo-beach" role="img" aria-label="Foto: Strand durch den Zelteingang gesehen"><span class="seal"></span></div>
    <div class="card-body">
      <div class="card-stars"><svg width="80" height="14" viewBox="0 0 105 19"><g fill="#1d2557"><use href="#st"/><use href="#st" x="21"/><use href="#st" x="42"/><use href="#st" x="63"/><use href="#st" x="84"/></g></svg></div>
      <h3 class="card-name">Camping Elbufer Strand</h3>
      <div class="card-place">⚲ 21499 Elbmarsch</div>
      <div class="breadcrumb"><span>Deutschland</span><span>›</span><span>Niedersachsen</span><span>›</span><span>Lüneburger Heide</span></div>
      <p class="card-text">Der Campingplatz Elbufer Strand ist ein ebener Campingplatz direkt an der Elbe mit gepflegtem Wiesengelände und einem kleinen Teich.</p>
    </div>
    <div class="card-foot"><span class="card-price">VERGLEICHSPREIS: <b>25,00 €</b></span><a class="card-more">MEHR DAZU</a></div>
  </div>

  <div class="abs card" style="left:449px">
    <div class="card-img img-mountain" role="img" aria-label="Foto: Zelte auf einer Wiese vor Berghängen"><span class="seal"></span></div>
    <div class="card-body">
      <div class="card-stars"><svg width="80" height="14" viewBox="0 0 105 19"><g fill="#1d2557"><use href="#st"/><use href="#st" x="21"/><use href="#st" x="42"/><use href="#st" x="63"/><use href="#st" x="84"/></g></svg></div>
      <h3 class="card-name">Spessart-Camping Waldblick</h3>
      <div class="card-place">⚲ 97799 Talhausen</div>
      <div class="breadcrumb"><span>Deutschland</span><span>›</span><span>Bayern</span><span>›</span><span>Spessart</span></div>
      <p class="card-text">Der Campingplatz ist parzelliert und terrassenartig angelegt. Die Gelände ist teils durch Bäume, teils durch Gebüsch charakterisiert.</p>
    </div>
    <div class="card-foot"><span class="card-price">VERGLEICHSPREIS: <b>31,11 €</b></span><a class="card-more">MEHR DAZU</a></div>
  </div>

  <div class="abs card" style="left:774px">
    <div class="card-img img-forest" role="img" aria-label="Foto: Bäume und Wiese an einem Campingplatz"><span class="seal"></span></div>
    <div class="card-body">
      <div class="card-stars"><svg width="48" height="14" viewBox="0 0 63 19"><g fill="#1d2557"><use href="#st"/><use href="#st" x="21"/><use href="#st" x="42"/></g></svg></div>
      <h3 class="card-name">Camping Seeblick</h3>
      <div class="card-place">⚲ 4399 Duinkerk</div>
      <div class="breadcrumb"><span>Niederlande</span><span>›</span><span>Zeeland</span><span>›</span><span>Zeeland</span></div>
      <p class="card-text">Der Campingplatz Camping Seeblick ist ein ebenes Wiesengelände.<br>Die Stellplätze sind durch Hecken parzelliert.</p>
    </div>
    <div class="card-foot"><span class="card-price">VERGLEICHSPREIS: <b>25,00 €</b></span><a class="card-more">MEHR DAZU</a></div>
  </div>
</section>

<section class="abs directory">
  <h2 class="abs dir-title">Campingplatz Auswahl</h2>
  <div class="abs dir-group" style="left:124px;top:76px;width:430px">
    <h4>Länder Auswahl</h4>
    <a>Campingplätze Deutschland</a><a>Campingplätze Belgien</a><a>Campingplätze Dänemark</a><br>
    <a>Campingplätze England</a><a>Campingplätze Frankreich</a><a>Campingplätze Italien</a><br>
    <a>Campingplätze Niederlande</a><a>Campingplätze Schweiz</a><a>Campingplätze Spanien</a><br>
    <a>Campingplätze Österreich</a>
  </div>
  <div class="abs dir-group" style="left:124px;top:176px;width:440px">
    <h4>Bundesländern in</h4>
    <a>Campingplätze Baden-Württemberg</a><a>Campingplätze Bayern</a><br>
    <a>Campingplätze Nordrhein-Westfalen</a><a>Campingplätze Niedersachsen</a><br>
    <a>Campingplätze Berlin</a><a>Campingplätze Brandenburg</a><a>Campingplätze Bremen</a><br>
    <a>Campingplätze Hamburg</a><a>Campingplätze Hessen</a><br>
    <a>Campingplätze Mecklenburg-Vorpommern</a><a>Campingplätze Rheinland-Pfalz</a><br>
    <a>Campingplätze Saarland</a><a>Campingplätze Sachsen</a><a>Campingplätze Sachsen-Anhalt</a><br>
    <a>Campingplätze Schleswig-Holstein</a><a>Campingplätze Thüringen</a>
  </div>
  <div class="abs dir-group" style="left:672px;top:80px;width:420px">
    <h4>Regionen in</h4>
    <a>Campingplätze Aachener Land</a><a>Campingplätze Ahrtal</a><a>Campingplätze Ahrtal</a><br>
    <a>Campingplätze Allgäu</a><a>Campingplätze Allgäu</a><a>Campingplätze Alpen</a><br>
    <a>Campingplätze Alpen</a><a>Campingplätze Altenahr</a><a>Campingplätze Altenburg</a><br>
    <a>Campingplätze Altmark</a><a>Campingplätze Altmark</a><a>Campingplätze Altmark bis Halle</a><br>
    <a>Campingplätze Altmark bis Halle</a><a>Campingplätze Altmühltal</a><br>
    <a>Campingplätze Ammerland</a><a>Campingplätze Amrum</a><a>Campingplätze Aschaffenburg</a><br>
    <a>Campingplätze Augsburg</a><a>Campingplätze Bad Hersfeld</a><br>
    <a>Campingplätze Bad Kissingen</a><a>Campingplätze Bad Kösen</a><br>
    <a>Campingplätze Bad Saarow</a><a>Campingplätze Bad Schandau</a><a>Campingplätze Bad Tölz</a><br>
    <a>Campingplätze Baden</a><a>Campingplätze Bamberg</a><a>Campingplätze Barnimer Land</a><br>
    <a>Campingplätze Bautzen</a><a>Campingplätze Bayerischer Wald</a><br>
    <a>Campingplätze Berchtesgadener Land</a>
  </div>
  <div class="abs ad-banner">
    <div class="ad-big">Book A Hotel Tonight</div>
    <div class="ad-small" style="font-size:12px;line-height:16px;margin-top:2px">example.com<br>Special Rates Until the End of the Month. No Booking Fees.</div>
    <span class="ad-go abs"></span>
  </div>
  <div class="abs ad-note">Werbung</div>
</section>

<section class="abs shop-band">
  <p class="abs shop-text display">Besuchen Sie unseren Shop und sichern Sie sich 10% Neukundenrabatt!</p>
  <a class="abs btn-shop">ZUM SHOP</a>
</section>

<footer class="abs site-footer">
  <div class="abs footer-brand"><span class="brand-mark" style="width:28px;height:28px"></span><span class="brand-name">zeltfuchs</span></div>
  <div class="abs footer-col" style="left:429px"><h3>Unser Service</h3><ul><li>Campingplätze</li><li>Campingblog</li><li>Campingplatz anmelden</li></ul></div>
  <div class="abs footer-col" style="left:654px"><h3>Über zeltfuchs</h3><ul><li>Über uns</li><li>Kontakt</li><li>Sitemap</li></ul></div>
  <div class="abs footer-col" style="left:913px"><h3>Follow us</h3></div>
  <div class="abs social"><i></i><i></i><i></i><i></i></div>
</footer>

<div class="abs bottom-bar">
  <span style="left:124px">© Copyright 2017</span>
  <span style="left:953px">Datenschutz | Impressum</span>
</div>

</body>
</html>
```